US company marketing to law enforcement needs brochure design

We have created a new logo and now need to update our printed material. What we really need is a "style" or "template" for how our brochures will look in the future. Enclosed is the brochure draft with the old style and logo. Also enclosed is the new logo. As we are marketing to US law enforcement it is important the the brochure design is strong, powerful and that we are looking experienced and trustworthy. However, we also want to look modern in line with the logo update.

Target Market(s)

Law enforcement

Industry/Entity Type

Marketing

```html
<!DOCTYPE html>
<html lang="en">
<head>
<meta charset="utf-8">
<title>Calderwick Solutions – Comprehensive Offender Solutions</title>
<link rel="stylesheet" href="https://fonts.googleapis.com/css2?family=Questrial&family=Arimo:wght@400;700&display=swap">
<style>
:root{
  --navy:#2f3a73;
  --grey:#a6a6a6;
  --grey-dark:#8a8a8a;
  --grey-light:#cfcfcf;
  --white:#ffffff;
  --menu-text:#e4e7f1;
  --text-dark:#3a3a3a;
}
*{margin:0;padding:0;box-sizing:border-box}
html,body{width:1200px;height:776px;overflow:hidden;background:var(--white)}
.canvas{position:relative;width:1200px;height:776px;overflow:hidden;background:var(--white);font-family:"Arimo",Arial,sans-serif}
.abs{position:absolute}

/* header */
.brand-panel{left:0;top:0;width:670px;height:158px;background:var(--navy);border-bottom-right-radius:22px}
.brand-mark{left:68px;top:30px;width:78px;height:78px;border-radius:50%;background:var(--white)}
.brand-name{left:168px;top:46px;font-family:"Questrial",sans-serif;font-size:37px;color:var(--grey-light);letter-spacing:.3px;white-space:nowrap}
.title-bar{left:672px;top:18px;width:528px;height:44px;background:var(--navy);color:var(--white);font-family:"Questrial",sans-serif;font-size:28px;text-align:center;line-height:44px;letter-spacing:.4px}
.subtitle-band{left:672px;top:66px;width:528px;height:92px;background:var(--grey);color:var(--navy);font-family:"Questrial",sans-serif;font-size:23px;text-align:center;line-height:30px;padding-top:16px;letter-spacing:.2px}

/* sidebar */
.sidebar{left:0;top:158px;width:338px;height:618px;background:linear-gradient(90deg,#9e9e9e,#b0b0b0)}
.stage-list{left:0;top:178px;list-style:none;width:350px}
.stage-list li{position:relative;height:35.5px;font-family:"Questrial",sans-serif;font-size:20px;color:var(--white);padding-left:32px;line-height:32px;letter-spacing:.4px}
.stage-list li::after{content:"";position:absolute;left:0;bottom:4px;width:130px;height:1px;background:rgba(255,255,255,.8)}
.stage-list li::before{content:"";position:absolute;left:245px;bottom:13px;width:100px;height:3px;background:linear-gradient(90deg,rgba(47,58,115,.9),rgba(47,58,115,0))}
.emblem-ring{left:83px;top:432px;width:162px;height:162px;border-radius:50%;background:var(--white);box-shadow:0 2px 6px rgba(0,0,0,.25)}
.emblem-core{left:90px;top:439px;width:148px;height:148px;border-radius:50%;background:var(--navy)}
.emblem-shadow{left:105px;top:622px;width:118px;height:6px;border-radius:50%;background:radial-gradient(rgba(80,80,80,.45),rgba(80,80,80,0))}

/* feature panel */
.feature-photo{left:352px;top:166px;width:848px;height:376px;background:linear-gradient(100deg,#e9e6e2 0%,#d9cfc4 30%,#eeeae6 55%,#c9ccd3 80%,#dfe1e6 100%)}
.feature-wash{left:352px;top:166px;width:848px;height:376px;background:linear-gradient(180deg,rgba(255,255,255,.55),rgba(255,255,255,.25))}
.feature-heading{left:388px;top:201px;font-family:"Questrial",sans-serif;font-size:19px;color:var(--navy);letter-spacing:.3px;white-space:nowrap}
.feature-heading strong{font-weight:700}
.fit-pill{left:830px;top:180px;width:344px;height:62px;border-radius:22px;background:var(--grey-dark);color:var(--white);font-family:"Questrial",sans-serif;font-size:15px;line-height:18px;padding:5px 0 0 24px;border:1px solid rgba(255,255,255,.6)}
.feature-block h3{font-family:"Questrial",sans-serif;font-weight:400;font-size:16px;color:var(--navy);margin-bottom:6px;letter-spacing:.2px}
.feature-block p{font-size:12.4px;line-height:17px;color:var(--text-dark);text-align:justify;background:rgba(255,255,255,.55);border-radius:8px;padding:2px 2px 2px 0;margin-bottom:6px}
.block-exp{left:380px;top:252px;width:372px}
.block-save{left:768px;top:252px;width:414px}
.block-control{left:380px;top:378px;width:364px}
.block-tech{left:768px;top:378px;width:414px}

/* bottom */
.bottom-panel{left:338px;top:542px;width:862px;height:234px;background:var(--navy)}
.tab{height:30px;background:linear-gradient(180deg,#f4f4f4,#c9c9c9);color:var(--navy);font-family:"Questrial",sans-serif;font-size:20px;line-height:30px;padding-left:6px;letter-spacing:.3px;white-space:nowrap}
.tab::after{content:"";position:absolute;right:0;top:0;width:12px;height:30px;background:#9e9e9e}
.tab-arrow{position:absolute;right:3px;top:10px;width:0;height:0;border-top:5px solid transparent;border-bottom:5px solid transparent;border-left:6px solid var(--white);z-index:1}
.tab-custom{left:338px;top:553px;width:234px}
.tab-admin{left:338px;top:645px;width:465px}
.custom-copy{left:350px;top:592px;width:445px;font-size:16.5px;line-height:25px;color:var(--white)}
.service-row{left:350px;font-size:16.5px;color:var(--white);display:flex;gap:12px;white-space:nowrap}
.service-row span::before{content:"";display:inline-block;width:7px;height:7px;background:var(--white);margin-right:4px;vertical-align:2px}
.row-one{top:687px}
.row-two{top:729px}
.row-two{gap:16px}
.menu-card{left:836px;top:520px;width:340px;height:62px;border-radius:8px;background:linear-gradient(180deg,#fff 55%,#d2d2d2);box-shadow:0 2px 4px rgba(0,0,0,.3);text-align:center;font-family:"Questrial",sans-serif;font-size:20px;color:var(--navy);padding-top:17px;letter-spacing:.3px}
.menu-caret{left:1000px;top:569px;width:0;height:0;border-left:5px solid transparent;border-right:5px solid transparent;border-top:6px solid var(--navy)}
.menu-list{left:858px;top:588px;list-style:none;font-size:15px;line-height:18.9px;color:var(--menu-text);white-space:nowrap}
.menu-list li::before{content:"";display:inline-block;width:8px;height:8px;border-radius:50%;background:#9a9fb4;margin-right:5px;vertical-align:1px}
.dot{display:inline-block;width:8px;height:8px;border-radius:50%;background:#9a9fb4;margin:0 3px;vertical-align:1px}
</style>
</head>
<body>
<div class="canvas">

  <div class="abs brand-panel"></div>
  <div class="abs brand-mark"></div>
  <div class="abs brand-name">Calderwick Solutions</div>

  <div class="abs title-bar">Comprehnsive Offender Solutions</div>
  <div class="abs subtitle-band">We Administer Offender Programs at every<br>Stage of the Criminal Justice Process</div>

  <div class="abs sidebar"></div>
  <ul class="abs stage-list">
    <li>Pre-Trial</li>
    <li>Diversion</li>
    <li>Deferred Prosecution</li>
    <li>Jail Alternative</li>
    <li>Probation</li>
  </ul>
  <div class="abs emblem-ring"></div>
  <div class="abs emblem-core"></div>
  <div class="abs emblem-shadow"></div>

  <div class="abs feature-photo" role="img" aria-label="Soft-focus photograph of professionals meeting around a desk"></div>
  <div class="abs feature-wash"></div>

  <div class="abs feature-heading"><strong>Flexible Solutions For</strong> Your Jurisdiction’s Needs</div>
  <div class="abs fit-pill">NOT A ONE-SIZE FITS ALL SOLUTION:<br>EACH PROGRAM DEVELOPED AND<br>ADMINISTERED TO YOUR SPECIFICATIONS.</div>

  <div class="abs feature-block block-exp">
    <h3>EXPERIENCED PROFESSIONALS</h3>
    <p>'Calderwick Solutions' core management and operations team has over 25+ years of experience developing and administering programs for prosecutors, courts an probation. Each program has unique requirements for the participants based on the goals of each jurisdiction.</p>
  </div>
  <div class="abs feature-block block-save">
    <h3>SAVE RESOURCES / REDUCE CASE LOADS</h3>
    <p>'Calderwick Solutions' provies the resources to reduce your staff's workload and facilitate a quick resolution to cases. Our staff handles all program administrative responsibilities from case referral to resolution and reporting.</p>
  </div>
  <div class="abs feature-block block-control">
    <h3>CONTROL / TRANSPARENCY</h3>
    <p>Your office establishes the parameters and offender requirements for each program and always maintains the control to change program guidelines at anytime.</p>
    <p>'Calderwick Solutions' provides you and your designated staff with 24x7 online access to all case files that contain a record of every action take on each case</p>
  </div>
  <div class="abs feature-block block-tech">
    <h3>TECHNOLOGY / EQUIPMENT</h3>
    <p>'Calderwick Solutions' utilizes technology to automate process that in turn allows our staff to focus on interactions with the offenders. When electronic monitoring is required, Calderwick Solutions uses only the latest and most current equipment models to ensure the accurate offender accountability and public safety.</p>
  </div>

  <div class="abs bottom-panel"></div>

  <div class="abs tab tab-custom">CUSTOM SOLUTIONS<span class="tab-arrow"></span></div>
  <div class="abs custom-copy">All offender programs are customized to meet the unique needs of your jurisictions.</div>

  <div class="abs tab tab-admin">COMPREHENSIVE ADMINISTRATIVE SERVICES<span class="tab-arrow"></span></div>
  <div class="abs service-row row-one"><span>Eligible case screening</span><span>Case referral</span><span>Data entry</span></div>
  <div class="abs service-row row-two"><span>Electronic case files</span><span>Offender communication</span><span>Reporting</span></div>

  <div class="abs menu-card">FULL MENU OF CONDITIONS</div>
  <div class="abs menu-caret"></div>
  <ul class="abs menu-list">
    <li>Case Management <span class="dot"></span>Face to face meetings</li>
    <li>Offender Education <span class="dot"></span>Group counseling</li>
    <li>Fine and Fee Recovery <span class="dot"></span>Victim Restitution</li>
    <li>Recovery Inter-active <span class="dot"></span>Joumaling Drug</li>
    <li>Drug testing <span class="dot"></span>Community Resource Referrals</li>
    <li>Alcohol monitoring <span class="dot"></span>Community Service</li>
    <li>GP monitoring <span class="dot"></span>Curfew monitoring</li>
    <li>Home detention <span class="dot"></span>Offender communication</li>
    <li>Preparation of court paperwork <span class="dot"></span>Reporting</li>
  </ul>

</div>
</body>
</html>
```